Business Card Design

i am looking a business card for a car rental company long with Taxi service also a logo.

what is the latest with my project

Industry/Entity Type

Business

Contact Information for Business Card

name of the Company is Kestrel Bay Motor Leasing and Taxi Services
Address: Palm Hollow Road, Leeward Parish Antigua
Tele# 555-0142/5550187-555-0163
Email: lorimbeck@quillmarsh.test

Font styles to use
Script

```html
<!DOCTYPE html>
<html lang="en">
<head>
<meta charset="utf-8">
<title>Kestrel Bay – Business Card</title>
<link rel="stylesheet" href="https://fonts.googleapis.com/css2?family=Tinos:wght@400;700&display=swap">
<style>
  :root {
    --ink: #050505;
    --gold: #d89413;
    --rule: #5a4a2a;
    --backdrop: #e9e4da;
  }
  * { margin: 0; padding: 0; box-sizing: border-box; }
  html, body {
    width: 1200px; height: 800px; overflow: hidden;
    background: var(--backdrop);
  }
  .card {
    position: absolute; left: 100px; top: 114px;
    width: 1000px; height: 572px;
    background: var(--gold);
    box-shadow: 0 10px 30px rgba(0,0,0,.25);
    overflow: hidden;
    font-family: "Tinos", "Times New Roman", serif;
    color: var(--ink);
  }
  .card__panel { position: absolute; left: 0; top: 0; width: 460px; height: 572px; }
  .card__brand { position: absolute; left: 500px; top: 92px; }
  .brand__name { font-size: 66px; font-weight: 700; letter-spacing: 3px; line-height: 1; }
  .brand__tagline { font-size: 22px; margin-top: 6px; letter-spacing: .5px; }
  .card__rule {
    position: absolute; left: 460px; right: 0; height: 1px; background: var(--rule);
  }
  .contact { position: absolute; left: 500px; font-size: 24px; letter-spacing: .5px; white-space: nowrap; }
  .contact--phone span + span { margin-left: 56px; }
</style>
</head>
<body>
  <div class="card">
    <svg class="card__panel" width="460" height="572" viewBox="0 0 460 572">
      <rect class="panel__fill" width="460" height="572" fill="var(--ink)"/>
      <polygon class="panel__collar" points="0,0 55,0 120,80 0,125" fill="var(--gold)"/>
      <g class="panel__icons" fill="none" stroke="var(--gold)" stroke-width="2">
        <circle cx="420" cy="296" r="18"/>
        <path d="M413 289c0 9 5 14 14 14l3-4-4-3-2 2c-3-1-5-3-6-6l2-2-3-4z" fill="var(--gold)" stroke="none"/>
        <circle cx="420" cy="351" r="18"/>
        <rect x="410" y="344" width="20" height="14" fill="var(--gold)" stroke="none"/>
        <path d="M410 344l10 8 10-8" stroke="var(--ink)" stroke-width="1.5"/>
        <circle cx="420" cy="406" r="18"/>
        <path d="M420 418c-6-7-8-10-8-14a8 8 0 0 1 16 0c0 4-2 7-8 14z" fill="var(--gold)" stroke="none"/>
        <circle cx="420" cy="404" r="2.5" fill="var(--ink)" stroke="none"/>
      </g>
    </svg>

    <div class="card__brand">
      <div class="brand__name">Kestrel Bay</div>
      <div class="brand__tagline">Motor Leasing and Taxi Services</div>
    </div>

    <div class="card__rule" style="top:262px"></div>
    <div class="contact contact--phone" style="top:282px"><span>555-0142/5550</span><span>187-555-0163</span></div>
    <div class="card__rule" style="top:322px"></div>
    <div class="contact contact--email" style="top:337px">lorimbeck@quillmarsh.test</div>
    <div class="card__rule" style="top:376px"></div>
    <div class="contact contact--address" style="top:392px">Palm Hollow Road, Leeward Parish Antigua</div>
    <div class="card__rule" style="top:432px"></div>
    <div class="card__rule" style="top:442px"></div>
  </div>
</body>
</html>
```